Wordpress Design For Financial Investment Company

//** NEW WIREFRAME ADDED TO HELP WITH LAYOUT ISSUES. PLEASE REFER TO WIREFRAME IN ATTACHED FILES. NO DESIGN WILL BE CONSIDERED IF IT DOES NOT FOLLOW THE WIREFRAME. **//
//** PLEASE READ THE ENTIRE BRIEF INCLUDING ALL UPDATES TO THE BRIEF. THE CLIENT IS VERY SPECIFIC ABOUT WHAT THEY WANT AND I'VE COVERED SEVERAL THINGS IN THE UPDATES. THERE IS ALSO A VIDEO UPDATE THAT HAS SOME VALUABLE INFORMATION IN IT FOR THIS CONTEST. **//
The client is an investment advisor who needs a new website designed. The current site is http://www.veltorbay.net.
The client wants the site to be green to match the attached logo.
The home page should have relevant images in the rotator. No people hugging! This is a financial investment site, not a family counseling site.
Also, the client wants 4 buttons on the home page to highlight the 4 main areas they focus on:
Investment Advice and Education
General Financial Planning
Retirement Planning
401K Planning
The top right area of the site needs to have their phone number, a call to action, and 2 buttons.
Their phone number is 303-481-7294
The call to action should say something like "Call for a free consultation!"
The buttons need to say:
Login To Your Quellbrook Account
Login To Your Halvenpoint Account
The final design should communicate professionalism, financial safety and growth.
Main navigation should be:
Home
About Us
Associates
Services
Contact
Mission Statement (Could also be "Our Mission")
This is a site that the client likes: http://www.pmrwealthguidance.com/
Updates
The designs should not have:
Newsletter content. A newsletter sign up is fine
Learning Center
Calculators
Stock prices/tickers
The design should have a contact form on the page.
I have talked to my client and have some updates. I did a video update because I thought it would be easier to show what I'm trying to get across.
Reason: I am going to be extending the contest a few more days. I'm still not getting quite what I want and very few people are even trying to follow the creative brief and the updates to it.
PLEASE read the entire brief and the updates. There is also a video I made that explains everything. I've also attached a wireframe.
Thanks!
Target Market(s)
People looking for a high-end financial investment company.
Industry/Entity Type
Investment
Requirements
Must have
- !!FOLLOW THE WIREFRAME FOR LAYOUT!!
!!THEIR LOGO!!
4 buttons to highlight their main practice areas
Phone number in the top right
"Free Consultation" call to action
2 Login buttons in the top right
A contact form on the page.
Should not have
- The designs should not have:
Learning Center
Calculators
Stock prices/tickers

```html
<!DOCTYPE html>
<html lang="en">
<head>
<meta charset="utf-8">
<title>Veltorbay Financial</title>
<link href="https://fonts.googleapis.com/css2?family=Montserrat:wght@400;500;600;700&family=Nunito+Sans:wght@400;600;700&family=Crimson+Text:ital,wght@1,400;1,600&display=swap" rel="stylesheet">
<style>
:root{
  --green:#2f6d67;
  --green-dark:#24524e;
  --cream:#fdf8f0;
  --white:#ffffff;
  --ink:#1d1d1d;
  --text:#4a4a4a;
  --rust:#c8632f;
  --orange:#f99a12;
  --orange-light:#fbb52a;
  --tan:#c3a797;
  --footer:#ece6e0;
  --line:#d6cfc8;
}
*{box-sizing:border-box;margin:0;padding:0}
html,body{width:1200px;height:1122px;overflow:hidden}
body{position:relative;background:var(--cream);font-family:"Nunito Sans",sans-serif;color:var(--text)}
.abs{position:absolute}

/* header */
.topbar{left:0;top:0;width:1200px;height:101px;background:var(--white)}
.agent-photo{left:142px;top:0;width:98px;height:101px;background:linear-gradient(180deg,#e9c3a8,#d88f7a 70%,#e4a08e)}
.cta{left:242px;top:28px;font-family:"Crimson Text",serif;font-style:italic;font-size:16.5px;color:#555;white-space:nowrap}
.phone{left:242px;top:44px;font-family:"Montserrat",sans-serif;font-weight:500;font-size:34px;color:var(--ink);white-space:nowrap}
.login{top:17px;width:192px;height:63px;border-radius:4px;color:var(--white);font-family:"Montserrat",sans-serif;font-size:13px;font-weight:500;line-height:17px;padding:14px 0 0 10px;white-space:nowrap}
.login-a{left:664px;background:linear-gradient(180deg,#d98a55,#b7693a)}
.login-b{left:865px;background:linear-gradient(180deg,#ffc20e,#ff9500)}

/* nav */
.navband{left:0;top:101px;width:1200px;height:105px;background:var(--green)}
.nav a{position:absolute;top:145px;font-family:"Montserrat",sans-serif;font-weight:600;font-size:15px;color:var(--white);text-decoration:none;letter-spacing:.3px}
.brand{left:522px;top:74px;width:156px;height:156px;border-radius:50%;background:var(--white);display:flex;align-items:center;justify-content:center}
.brand-ring{width:140px;height:140px;border-radius:50%;background:#efe6de;border:4px solid var(--green-dark);display:flex;flex-direction:column;align-items:center;justify-content:center;font-family:"Montserrat",sans-serif;font-weight:700;color:var(--green-dark);text-align:center}
.brand-ring .n1{font-size:17px;letter-spacing:1px}
.brand-ring .n2{font-size:11px;margin-top:3px}

/* intro */
.quote{left:0;top:228px;width:1200px;text-align:center;font-family:"Crimson Text",serif;font-style:italic;font-weight:600;font-size:35px;color:var(--ink)}
.advisor-photo{left:150px;top:286px;width:300px;height:420px;border-radius:120px 120px 0 0;background:linear-gradient(180deg,#e7d3c2 0%,#c9c6c1 30%,#b7b5b1 70%,#d6d3ce)}
.slider-dots{left:226px;top:678px;width:102px;height:34px;border-radius:17px 17px 0 0;background:var(--orange-light);display:flex;gap:4px;justify-content:center;padding-top:10px}
.slider-dots span{width:10px;height:10px;border-radius:50%;border:1.5px solid var(--white)}

.service{width:260px}
.service .kicker{font-family:"Crimson Text",serif;font-style:italic;font-size:24px;color:#555;line-height:26px}
.service h2{font-family:"Montserrat",sans-serif;font-weight:500;font-size:19.5px;color:var(--rust);line-height:26px;white-space:nowrap}
.service p{margin-top:12px;font-size:14px;line-height:20.5px;color:var(--text)}
.service a{display:block;color:var(--rust);text-decoration:none}

/* newsletter band */
.newsband{left:0;top:706px;width:1200px;height:62px;background:linear-gradient(180deg,var(--orange-light),var(--orange) 40%,#fb8a0a)}
.env{left:150px;top:716px}
.news-intro{left:216px;top:722px;font-size:12px;color:var(--ink);white-space:nowrap}
.news-title{left:216px;top:740px;font-family:"Montserrat",sans-serif;font-weight:600;font-size:13.5px;color:var(--white);white-space:nowrap}
.news-input{left:488px;top:725px;width:165px;height:27px;background:var(--white);border:1px solid #ddd;font-size:12.5px;padding:5px 7px;color:#333}
.news-submit{left:653px;top:725px;width:64px;height:27px;background:#161616;border-radius:0 4px 4px 0;color:var(--white);font-family:"Montserrat",sans-serif;font-weight:700;font-size:12px;text-align:center;line-height:27px}
.stay{left:742px;top:726px;font-family:"Montserrat",sans-serif;font-weight:600;font-size:17.5px;color:var(--ink);white-space:nowrap}
.social{top:716px;width:43px;height:43px;border-radius:50%;background:var(--white)}

/* footer */
.footer{left:0;top:768px;width:1200px;height:354px;background:var(--footer)}
.fhead{top:797px;height:24px;background:var(--tan);color:var(--white);font-family:"Montserrat",sans-serif;font-weight:500;font-size:14px;line-height:24px;padding:0 10px}
.flist{list-style:none;font-size:12.5px;color:var(--ink)}
.flist li{height:24.4px;line-height:18px}
.divider{top:797px;width:1px;height:247px;background:var(--line)}
.contact{left:599px;top:836px;font-size:12.5px;color:var(--ink);line-height:16.5px}
.contact dt{font-weight:700;color:#8a6d58}
.contact dd{margin-bottom:15px}
.field{left:839px;width:210px;background:#f8f5f1;border:1px solid #d9d2cb;font-size:12.5px;color:#333;padding:5px 9px}
.send{left:839px;top:1013px;width:74px;height:28px;background:var(--rust);color:var(--white);font-family:"Montserrat",sans-serif;font-weight:600;font-size:16px;text-align:center;line-height:28px}
.rule{left:142px;top:1063px;width:916px;height:1px;background:var(--line)}
.copy{left:0;top:1078px;width:1200px;text-align:center;font-size:12px;color:var(--ink)}
</style>
</head>
<body>

<div class="abs topbar"></div>
<div class="abs agent-photo" role="img" aria-label="Support agent with headset"></div>
<div class="abs cta">CALL FOR A FREE CONSULTATION!</div>
<div class="abs phone">303-481-7294</div>
<a class="abs login login-a">Login to<br>Your Halvenpoint Account</a>
<a class="abs login login-b">Login to<br>Your Quellbrook Account</a>

<div class="abs navband"></div>
<nav class="nav">
  <a style="left:140px">HOME</a>
  <a style="left:236px">ABOUT US</a>
  <a style="left:364px">ASSOCIATES</a>
  <a style="left:714px">SERVICES</a>
  <a style="left:836px">OUR MISSION</a>
  <a style="left:986px">CONTACT</a>
</nav>
<div class="abs brand">
  <div class="brand-ring"><span class="n1">VELTORBAY</span><span class="n2">Financial, Inc.</span></div>
</div>

<div class="abs quote">“Always do right. This will gratify some people &amp; astomish the rest.”</div>

<div class="abs advisor-photo" role="img" aria-label="Smiling advisor in a grey suit pointing to the services"></div>
<div class="abs slider-dots"><span></span><span></span><span></span><span></span><span></span></div>

<section class="abs service" style="left:505px;top:298px">
  <div class="kicker">Investment</div>
  <h2>ADVICE &amp; EDUCATION</h2>
  <p>This is Photoshop's version &nbsp;of Lorem Ipsum. Proin gravida nibh vel velit auctor aliquet. Aenean sollicitudin, lorem quis bibendum auctor, nisi elit. <a>[Read More]</a></p>
</section>
<section class="abs service" style="left:816px;top:298px">
  <div class="kicker">General</div>
  <h2>FINANCIAL PLANNING</h2>
  <p>This is Photoshop's version &nbsp;of Lorem Ipsum. Proin gravida nibh vel velit auctor aliquet. Aenean sollicitudin, lorem quis bibendum auctor, nisi elit. <a>[Read More]</a></p>
</section>
<section class="abs service" style="left:505px;top:505px">
  <div class="kicker">Retirement</div>
  <h2>PLANNING</h2>
  <p>This is Photoshop's version &nbsp;of Lorem Ipsum. Proin gravida nibh vel velit auctor aliquet. Aenean sollicitudin, lorem quis bibendum auctor, nisi elit. <a>[Read More]</a></p>
</section>
<section class="abs service" style="left:816px;top:505px">
  <div class="kicker">401K</div>
  <h2>401K PLANNING</h2>
  <p>This is Photoshop's version &nbsp;of Lorem Ipsum. Proin gravida nibh vel velit auctor aliquet. Aenean sollicitudin, lorem quis bibendum auctor, nisi elit. <a>[Read More]</a></p>
</section>

<div class="abs newsband"></div>
<svg class="abs env" width="50" height="46" viewBox="0 0 50 46" aria-hidden="true">
  <rect x="2" y="14" width="46" height="30" fill="#fde7b0" stroke="#b0782a" stroke-width="1.5"/>
  <rect x="10" y="2" width="30" height="28" fill="#fff" stroke="#9aa7b5" transform="rotate(-12 25 16)"/>
  <path d="M2 14 L25 32 L48 14" fill="none" stroke="#b0782a" stroke-width="1.5"/>
  <path d="M2 44 L20 28 M48 44 L30 28" stroke="#b0782a" stroke-width="1.5"/>
</svg>
<div class="abs news-intro">Enter your email to receive news &amp; updates.</div>
<div class="abs news-title">SIGN UP FOR OUR NEWSLETTERS</div>
<div class="abs news-input">Enter your email</div>
<div class="abs news-submit">SUBMIT</div>
<div class="abs stay">STAY CONNECT</div>
<a class="abs social" style="left:901px" aria-label="Social link"></a>
<a class="abs social" style="left:953px" aria-label="Social link"></a>
<a class="abs social" style="left:1004px" aria-label="Social link"></a>

<footer class="abs footer"></footer>
<div class="abs fhead" style="left:140px">SERVICES</div>
<ul class="abs flist" style="left:150px;top:836px">
  <li>Investment Advice &amp; Education</li>
  <li>General Financial Planning</li>
  <li>Retirement Planning</li>
  <li>401K Planning</li>
</ul>
<div class="abs divider" style="left:360px"></div>
<div class="abs fhead" style="left:398px">QUICK LINK</div>
<ul class="abs flist" style="left:408px;top:836px">
  <li>Home</li><li>About Us</li><li>Associates</li><li>Services</li><li>Our Mission</li><li>Contact</li>
</ul>
<div class="abs divider" style="left:542px"></div>
<div class="abs fhead" style="left:587px">CONTACT US</div>
<dl class="abs contact">
  <dt>Email Support:</dt><dd>hello@veltorbayfinancial.net</dd>
  <dt>Voice Support:</dt><dd>+303-481-7294</dd>
  <dt>Fax:</dt><dd>+303-557-1862</dd>
  <dt>Address:</dt><dd>Veltorbay Financial, Inc.<br>2840 Marlow Ridge Suite 410<br>Ashford Springs, CO 80246</dd>
</dl>
<div class="abs divider" style="left:800px"></div>
<div class="abs fhead" style="left:840px">CONTACT FORM</div>
<div class="abs field" style="top:834px;height:28px">Name</div>
<div class="abs field" style="top:871px;height:28px">Email</div>
<div class="abs field" style="top:908px;height:94px">Message</div>
<div class="abs send">SEND</div>

<div class="abs rule"></div>
<div class="abs copy">Copyright © 2013 Veltorbay. &nbsp;All Rights Reserved. &nbsp;| &nbsp;Privacy Policy &nbsp;| &nbsp;Terms &amp; Conditions</div>

</body>
</html>
```